New Human Resources Outsourcing company needs a brochure to explain services

I need a brochure that describes my business and the services we offer.

Everything we do is on my website as well. www.kelvornstaffing.com

Target Market(s)

Business Owners (Manufacturing, I.T. Financial Services)

Industry/Entity Type

Business

```html
<!DOCTYPE html>
<html lang="en">
<head>
<meta charset="utf-8">
<title>Kelvorn HR Solutions – Service Levels</title>
<link rel="stylesheet" href="https://fonts.googleapis.com/css2?family=Montserrat:wght@300;400;600;800&display=swap">
<style>
  :root {
    --stage: #d4d4d6;
    --paper: #ffffff;
    --purple: #7a3f8f;
    --purple-deep: #5b2c73;
    --lilac: #c9a6d6;
    --teal: #36b6aa;
    --grey: #6d6d6f;
    --ink: #2b2b2b;
    --ink-soft: #555555;
  }
  * { box-sizing: border-box; margin: 0; padding: 0; }
  html, body { width: 1200px; height: 960px; overflow: hidden; }
  body {
    background: var(--stage);
    font-family: "Montserrat", Arial, sans-serif;
    color: var(--ink);
    position: relative;
  }
  .flyer {
    position: absolute;
    left: 250px; top: 27px;
    width: 700px; height: 906px;
    background: var(--paper);
    overflow: hidden;
  }
  .swoosh { position: absolute; left: 0; width: 700px; }
  .swoosh--top { top: 0; height: 170px; }
  .swoosh--bottom { bottom: 0; height: 276px; }

  .brand {
    position: absolute; top: 55px; left: 0; width: 700px;
    display: flex; justify-content: center; align-items: center; gap: 14px;
  }
  .brand__mark { width: 44px; height: 44px; background: var(--purple); }
  .brand__name {
    font-weight: 400; font-size: 28px; letter-spacing: 3px;
    color: var(--purple-deep); text-transform: uppercase;
  }

  .intro {
    position: absolute; top: 150px; left: 30px; width: 640px;
    padding: 12px 20px;
    background: linear-gradient(180deg, rgba(201,166,214,0.35), rgba(255,255,255,0));
    font-size: 11px; font-weight: 400; text-transform: uppercase;
    text-align: center; line-height: 1.6; color: var(--ink-soft);
  }

  .tiers {
    position: absolute; top: 236px; left: 22px; width: 656px;
    display: flex; flex-direction: column; gap: 20px;
  }
  .tier { display: flex; align-items: center; }
  .tier__badge { position: relative; width: 150px; height: 80px; flex: none; }
  .tier__badge svg { position: absolute; left: 56px; top: 0; width: 80px; height: 80px; }
  .tier__name {
    position: absolute; left: 8px; top: 28px; font-weight: 800; font-size: 18px;
    color: var(--ink); letter-spacing: 0.5px;
  }
  .tier__card {
    flex: 1; margin-left: 18px; padding: 10px 14px;
    color: #fff; font-size: 11.5px; font-weight: 400; line-height: 1.55;
    border-radius: 3px; box-shadow: 0 3px 6px rgba(0,0,0,0.18);
  }
  .tier--premier .tier__card { background: var(--purple); }
  .tier--elite .tier__card { background: var(--teal); }
  .tier--deluxe .tier__card { background: var(--grey); }

  .functions { position: absolute; top: 648px; left: 30px; width: 640px; }
  .functions__title {
    font-weight: 800; font-size: 13px; color: #fff; text-transform: uppercase;
    letter-spacing: 0.5px; margin-bottom: 8px;
  }
  .functions__cols { display: flex; gap: 18px; }
  .functions__col { flex: 1; }
  .functions__col--mid { flex: 1.15; }
  .functions__col--wide { flex: 1.25; }
  .functions__label {
    display: inline-block; background: rgba(120,120,120,0.45); color: #fff;
    font-size: 9px; font-weight: 600; text-transform: uppercase; padding: 2px 8px;
    margin-bottom: 5px; min-width: 90px;
  }
  .functions__list { list-style: none; font-size: 10px; line-height: 1.4; color: var(--ink); }
  .functions__list li { white-space: nowrap; }
  .footnote {
    position: absolute; bottom: 64px; left: 30px; font-size: 9px; color: var(--ink);
  }
</style>
</head>
<body>
  <main class="flyer">
    <svg class="swoosh swoosh--top" viewBox="0 0 700 170" preserveAspectRatio="none" aria-hidden="true">
      <defs>
        <linearGradient id="topBand" x1="0" y1="0" x2="1" y2="0">
          <stop offset="0" stop-color="#7a3f8f"/>
          <stop offset="0.5" stop-color="#c9a6d6"/>
          <stop offset="1" stop-color="#6a3482"/>
        </linearGradient>
      </defs>
      <rect width="700" height="170" fill="url(#topBand)"/>
      <path d="M0 170 C 20 75, 200 28, 700 55 L700 170 Z" fill="#ffffff"/>
      <path d="M260 0 C 420 18, 560 27, 700 27" stroke="#e6d3ec" stroke-width="6" fill="none" opacity="0.7"/>
    </svg>

    <header class="brand">
      <span class="brand__mark"></span>
      <span class="brand__name">Kelvorn HR Solutions</span>
    </header>

    <p class="intro">After conducting your complimentary HR assessment, we work with you to bring your company into full compliance. For clients requiring ongoing HR support, we offer three service levels to choose from for a low monthly fee.</p>

    <div class="tiers">
      <section class="tier tier--premier">
        <div class="tier__badge">
          <svg viewBox="0 0 100 100"><path d="M32 18 A34 34 0 0 1 80 30 L92 50 L80 70 A34 34 0 0 1 32 82" fill="none" stroke="#7a3f8f" stroke-width="8" stroke-linejoin="round"/></svg>
          <span class="tier__name">PREMIER</span>
        </div>
        <p class="tier__card">This is our highest level of service providing your company's complete HR Department. We will handle Benefit Administration, Employee Relations and other HR functions. Your HR professional will come on site two days per week to handle all HR duties, meet with employees and partner with Management on strategic planning and organization development.</p>
      </section>

      <section class="tier tier--elite">
        <div class="tier__badge">
          <svg viewBox="0 0 100 100"><path d="M32 18 A34 34 0 0 1 80 30 L92 50 L80 70 A34 34 0 0 1 32 82" fill="none" stroke="#36b6aa" stroke-width="8" stroke-linejoin="round"/></svg>
          <span class="tier__name">ELITE</span>
        </div>
        <p class="tier__card">With this level of service your HR professional will come on site one day per week to handle all HR duties with most tasks being completed off-site. We will provide you with the tools and off-site support necessary to run an effective HR Department.</p>
      </section>

      <section class="tier tier--deluxe">
        <div class="tier__badge">
          <svg viewBox="0 0 100 100"><path d="M32 18 A34 34 0 0 1 80 30 L92 50 L80 70 A34 34 0 0 1 32 82" fill="none" stroke="#6d6d6f" stroke-width="8" stroke-linejoin="round"/></svg>
          <span class="tier__name">DELUXE</span>
        </div>
        <p class="tier__card">With this level of service your HR professional will come on site once per month and provide virtual HR support with most tasks and support being provided off-site. This level of service is ideal for companies who do not require an on-site presence and just need a back office and trusted partner to ensure they remain</p>
      </section>
    </div>

    <svg class="swoosh swoosh--bottom" viewBox="0 0 700 276" preserveAspectRatio="none" aria-hidden="true">
      <defs>
        <linearGradient id="lowBand" x1="0" y1="0" x2="0" y2="1">
          <stop offset="0" stop-color="#c9a6d6"/>
          <stop offset="0.6" stop-color="#f4ecf6"/>
          <stop offset="1" stop-color="#ffffff"/>
        </linearGradient>
        <linearGradient id="footBand" x1="0" y1="0" x2="1" y2="0">
          <stop offset="0" stop-color="#6a3482"/>
          <stop offset="0.55" stop-color="#c9a6d6"/>
          <stop offset="1" stop-color="#7a3f8f"/>
        </linearGradient>
      </defs>
      <rect x="0" y="0" width="700" height="225" fill="url(#lowBand)"/>
      <path d="M0 215 C 0 252, 60 262, 700 248 L700 276 L0 276 Z" fill="url(#footBand)"/>
      <path d="M0 150 C 10 220, 120 245, 700 232 L700 244 C 120 262, 0 240, 0 180 Z" fill="#ffffff" opacity="0.7"/>
    </svg>

    <section class="functions">
      <h2 class="functions__title">HR Functions Provided</h2>
      <div class="functions__cols">
        <div class="functions__col">
          <span class="functions__label">Benefits</span>
          <ul class="functions__list">
            <li>Benefits Administration</li>
            <li>COBRA Administration</li>
            <li>Worker's Comp Administration</li>
            <li>Affordable Care Act Compliance</li>
            <li>Leave of Absence Management</li>
          </ul>
        </div>
        <div class="functions__col functions__col--mid">
          <span class="functions__label">Human Resources</span>
          <ul class="functions__list">
            <li>Employee Onboarding</li>
            <li>Terminations/Separation Agreements</li>
            <li>Recruiting</li>
            <li>Performance Management</li>
            <li>Employee Relations</li>
            <li>Conflict Resolution</li>
            <li>Investigations</li>
            <li>Strategy and Development</li>
          </ul>
        </div>
        <div class="functions__col functions__col--wide">
          <span class="functions__label">Training</span>
          <ul class="functions__list">
            <li>Harassment Prevention</li>
            <li>From Buddy to Boss for New Supervisors</li>
            <li>Providing Effective Performance Reviews</li>
            <li>Various Safety Trainings</li>
            <li>CPR and First Aid</li>
            <li>Progressive Discipline</li>
          </ul>
        </div>
      </div>
    </section>

    <p class="footnote">*Additional fees apply</p>
  </main>
</body>
</html>
```